Wordpress Web Design for Coach/Consultant

I need a website for my business consulting and life coaching website.
Fully responsive website built on the WordPress self-hosted content management system
CMS Installation
Fully customized graphics and design
Customized slideshow presentation slides
Up to ten main navigation content tabs
SEO optimization
Contact form configuration
Customized favicon and social media icons
Photo gallery creation
Customized portfolio
Social media integration
Blog integration
Content sharing buttons
Subscription signup integration

Target Market(s)

Women Entrepreneurs

Industry/Entity Type

Life Coaching

Number of Pages Required

5+ page

Font styles to use
Sans Serif
Decorative

Colors
ec1f27
ffffff
000000

Requirements
Must have
• Fully responsive website built on the WordPress self-hosted content management system
• CMS Installation
• Fully customized graphics and design
• Customized slideshow presentation slides
• Up to ten main navigation content tabs
• SEO optimization
• Contact form configuration
• Customized favicon and social media icons
• Photo gallery creation
• Customized portfolio
• Social media integration
• Blog integration
• Content sharing buttons
• Subscription signup integration
Nice to have
• Here are a few sample websites to take a look at:
• www.maribelotway.com

```html
<!DOCTYPE html>
<html lang="en">
<head>
<meta charset="utf-8">
<title>Elle Marwood — Coaching for Women Entrepreneurs</title>
<link href="https://fonts.googleapis.com/css2?family=Lato:ital,wght@0,400;0,700;0,900;1,400&family=Great+Vibes&family=Cormorant+Garamond:ital,wght@0,500;1,500;1,600&display=swap" rel="stylesheet">
<style>
:root{
  --red:#ec1f27;
  --coral:#f0645a;
  --pink:#f39a98;
  --blush:#fbe3e3;
  --ink:#1a1a1a;
  --text:#555;
  --muted:#8a8a8a;
  --panel:#ececec;
  --line:#dcdcdc;
  --white:#ffffff;
  --footer:#8c8c8c;
  --s1:#3b5998;--s2:#1da1f2;--s3:#e4405f;--s4:#0077b5;--s5:#ff6600;--s6:#d44638;
}
*{box-sizing:border-box;margin:0;padding:0}
html,body{width:1200px;height:3228px;overflow:hidden;background:var(--white)}
body{font-family:'Lato',sans-serif;color:var(--text);position:relative}
.img{display:block;border-radius:2px}

/* header */
.site-header{height:128px;display:flex;align-items:center;justify-content:space-between;padding:0 120px}
.brand{font-family:'Lato',sans-serif;font-weight:900;font-size:52px;color:var(--red);letter-spacing:1px}
.social{display:flex;gap:8px}
.social span{width:26px;height:26px;display:block;border-radius:3px}

/* nav */
.main-nav{height:56px;background:var(--pink);display:flex;align-items:center;padding:0 120px;gap:46px}
.main-nav a{color:var(--white);font-weight:700;font-size:15px;text-decoration:none;letter-spacing:.5px}
.main-nav .search{margin-left:auto;width:230px;height:28px;border-radius:14px;background:rgba(255,255,255,.7)}

/* hero */
.hero{height:416px;position:relative;background:linear-gradient(100deg,#fff 0%,var(--blush) 45%,#fff 100%)}
.hero-photo{position:absolute;left:220px;top:0;width:250px;height:416px;background:linear-gradient(180deg,#6b4a3a 0%,#2d2d35 55%,#1d1d24 100%)}
.hero-name{position:absolute;left:545px;top:80px;font-family:'Great Vibes',cursive;font-weight:400;font-size:92px;color:var(--ink);line-height:1}
.hero-tag{position:absolute;left:545px;top:190px;font-family:'Cormorant Garamond',serif;font-size:56px;font-weight:500;color:var(--ink)}

/* intro */
.intro{height:420px;padding:40px 120px 0;position:relative}
.intro p{width:610px;font-size:14px;line-height:1.45;color:var(--text);margin-bottom:14px}
.intro-photo{position:absolute;left:800px;top:30px;width:180px;height:240px;background:linear-gradient(180deg,#d7a07c,#3b3b3b 60%,#c46b2a)}

/* join */
.join{margin:0 120px;height:68px;background:var(--panel);display:flex;align-items:center;justify-content:space-between;padding:0 40px 0 110px;gap:30px}
.join p{font-size:16px;color:var(--text);white-space:nowrap}
.join strong{color:var(--red);font-weight:400}
.btn{background:var(--coral);color:var(--white);font-weight:700;font-size:14px;letter-spacing:.5px;padding:14px 40px;display:inline-block;white-space:nowrap}

/* feature row */
.features{display:flex;gap:40px;margin:52px 120px 0;height:260px}
.feature-video{flex:1;position:relative;background:linear-gradient(120deg,#4d7d86,#b6c9bf 50%,#2f4b55)}
.feature-video .bar{position:absolute;left:0;right:0;bottom:0;height:26px;background:rgba(0,0,0,.55)}
.feature-event{flex:1;background:linear-gradient(160deg,#2c5ea8,#6b9ed6 55%,#d9b48a)}

/* articles + sidebar */
.content{display:flex;gap:40px;margin:40px 120px 0;height:740px}
.articles{width:640px}
.section-title{font-size:28px;font-weight:900;color:var(--ink);margin-bottom:28px}
.article{display:flex;gap:30px;margin-bottom:54px}
.article .img{width:220px;height:160px;flex:none}
.article h3{font-size:24px;font-weight:700;color:var(--ink);line-height:1.15;margin-bottom:8px}
.article .meta{font-size:12px;color:var(--red);margin-bottom:8px}
.article p{font-size:13px;line-height:1.45}
.sidebar{flex:1;padding-top:36px}
.widget-title{background:var(--coral);color:var(--white);font-weight:700;font-size:17px;padding:10px 16px;margin-bottom:18px}
.testimonial{text-align:center;margin-bottom:40px}
.avatar{width:80px;height:80px;border-radius:50%;margin:0 auto 12px;background:linear-gradient(160deg,#7a5340,#2c2c30)}
.testimonial h4{font-size:14px;color:var(--ink);font-weight:700;margin-bottom:8px}
.testimonial p{font-size:13px;line-height:1.45;margin-bottom:14px}
.dots{display:flex;justify-content:center;gap:8px}
.dots span{width:9px;height:9px;border-radius:50%;background:var(--line)}
.dots span:first-child{background:var(--coral)}
.subscribe p{font-size:13px;line-height:1.45;margin-bottom:14px}
.subscribe form{display:flex;margin-bottom:26px}
.subscribe .field{flex:1;height:40px;border:1px solid var(--line);padding:0 12px;font-size:12px;color:var(--muted);display:flex;align-items:center}
.subscribe .send{width:44px;height:40px;background:var(--ink);display:flex;align-items:center;justify-content:center}
.ad{height:240px;margin:0 10px;background:linear-gradient(170deg,#e7b400,#f4d34a 45%,#2d2d2d 75%,#ec1f27)}

/* book */
.book{margin:70px 120px 0;height:380px;background:var(--panel);position:relative}
.book-cover{position:absolute;left:60px;top:30px;width:220px;height:310px;background:linear-gradient(160deg,#f4f4f4,#c9c9c9)}
.book-copy{position:absolute;left:380px;top:40px;width:520px}
.book-copy h2{font-family:'Cormorant Garamond',serif;font-style:italic;font-weight:600;font-size:52px;color:var(--ink);line-height:1}
.book-copy h3{font-family:'Cormorant Garamond',serif;font-style:italic;font-weight:500;font-size:28px;color:var(--ink);margin:10px 0 14px}
.book-copy p{font-family:'Cormorant Garamond',serif;font-style:italic;font-size:17px;line-height:1.35;color:var(--text)}
.store-badge{position:absolute;right:60px;bottom:40px;width:130px;height:44px;background:var(--ink);border-radius:5px}

/* photo stream */
.stream h2{text-align:center;font-size:22px;font-weight:700;color:var(--ink);margin:80px 0 34px}
.stream-row{display:flex;margin:0 100px;height:170px}
.stream-row .img{flex:1;border-radius:0}

/* partners */
.partners{display:flex;justify-content:center;gap:90px;align-items:center;height:220px}
.partners span{font-weight:900;font-size:26px;color:#333;letter-spacing:1px}

.site-footer{position:absolute;left:0;right:0;bottom:0;height:48px;background:var(--footer);color:var(--white);font-size:12px;display:flex;align-items:center;justify-content:center}
</style>
</head>
<body>

<header class="site-header">
  <div class="brand">LOGO</div>
  <div class="social">
    <span style="background:var(--s1)"></span><span style="background:var(--s2)"></span><span style="background:var(--s3)"></span><span style="background:var(--s4)"></span><span style="background:var(--s5)"></span><span style="background:var(--s6)"></span>
  </div>
</header>

<nav class="main-nav">
  <a href="#">HOME</a><a href="#">ABOUT</a><a href="#">EVENT</a><a href="#">MEDIA</a><a href="#">STORY</a><a href="#">CONTACT</a>
  <div class="search"></div>
</nav>

<section class="hero">
  <div class="hero-photo img" role="img" aria-label="Portrait of the coach in a dark blazer, arms crossed"></div>
  <h1 class="hero-name">Elle Marwood</h1>
  <p class="hero-tag">Nunc fringilla dictum velit</p>
</section>

<section class="intro">
  <p>Lorem ipsum dolor sit amet, consectetur adipiscing elit. Mauris imperdiet laoreet quam at dapibus, nisl congue mi. Morbi ornare lacus a tortor, euismod vehicula nibh. Sed aliquet justo id pretium elementum. Ut porta, nisi at mattis tincidunt, nibh augue aliquet lacus, vel volutpat mi dui ullamcorper. Suspendisse rutrum neque sed lorem ultrices, quis maximus arcu gravida. Aliquam tristique non metus eu vestibulum. Praesent elementum vel risus ac ornare.</p>
  <p>Quisque eu pulvinar felis, in malesuada diam. Nunc et ex lacinia, tincidunt dui quis, lacinia augue. Integer convallis ipsum magna, non imperdiet tortor viverra at. Fusce aliquam pretium nibh, id pharetra orci auctor id. Vestibulum nisi elit, malesuada vitae maximus eu, maximus quis enim.</p>
  <div class="intro-photo img" role="img" aria-label="The coach seated on an orange office chair"></div>
</section>

<section class="join">
  <p>Join <strong>Elle Marwood's</strong> Network, Get the support and skills you need to go for it!</p>
  <a class="btn">JOIN NETWORK</a>
</section>

<section class="features">
  <div class="feature-video img" role="img" aria-label="Video still of a smiling woman outdoors"><div class="bar"></div></div>
  <div class="feature-event img" role="img" aria-label="Women entrepreneur summit banner with a city skyline"></div>
</section>

<section class="content">
  <div class="articles">
    <h2 class="section-title">Latest Artical</h2>
    <article class="article">
      <div class="img" role="img" aria-label="Woman at her desk looking unwell" style="background:linear-gradient(150deg,#9fc3df,#f1e3d4)"></div>
      <div><h3>5 Reasons You Should Never Go to Work Sick</h3><div class="meta">2023 June 21 &nbsp; Post by Ann Author</div><p>Quisque eu pulvinar felis, in malesuada diam. Nunc et ex lacinia, tincidunt dui quis, lacinia augue. Integer convallis ipsum magna, non imperdiet tortor viverra at. Fusce aliquam pretium nibh, id pharetra orci auctor id.</p></div>
    </article>
    <article class="article">
      <div class="img" role="img" aria-label="Woman working on a laptop in an office" style="background:linear-gradient(150deg,#e9e2d8,#5a4a44)"></div>
      <div><h3>5 Reasons You Should Never Go to Work Sick</h3><div class="meta">2023 June 21 &nbsp; Post by Ann Author</div><p>Quisque eu pulvinar felis, in malesuada diam. Nunc et ex lacinia, tincidunt dui quis, lacinia augue. Integer convallis ipsum magna, non imperdiet tortor viverra at. Fusce aliquam pretium nibh, id pharetra orci auctor id.</p></div>
    </article>
    <article class="article">
      <div class="img" role="img" aria-label="Group of women laughing together" style="background:linear-gradient(150deg,#d8b89a,#3e3030)"></div>
      <div><h3>5 Reasons You Should Never Go to Work Sick</h3><div class="meta">2023 June 21 &nbsp; Post by Ann Author</div><p>Quisque eu pulvinar felis, in malesuada diam. Nunc et ex lacinia, tincidunt dui quis, lacinia augue. Integer convallis ipsum magna, non imperdiet tortor viverra at. Fusce aliquam pretium nibh, id pharetra orci auctor id.</p></div>
    </article>
  </div>
  <aside class="sidebar">
    <h3 class="widget-title">Happy Clients</h3>
    <div class="testimonial">
      <div class="avatar img" role="img" aria-label="Client portrait"></div>
      <h4>Adrin Coley - Manager Northvale</h4>
      <p>Quisque eu pulvinar felis, in malesuada diam. Nunc et ex lacinia, tincidunt dui quis, lacinia augue. Integer convallis ipsum magna.</p>
      <div class="dots"><span></span><span></span><span></span><span></span></div>
    </div>
    <div class="subscribe">
      <h3 class="widget-title">Subscribe Newsletter</h3>
      <p>Quisque eu pulvinar felis, in malesuada diam. Nunc et ex lacinia tincidunt.</p>
      <form>
        <div class="field">Enter your Email</div>
        <div class="send"><svg width="18" height="18" viewBox="0 0 24 24"><path d="M2 21 23 12 2 3v7l15 2-15 2z" fill="#fff"/></svg></div>
      </form>
      <div class="ad img" role="img" aria-label="Promotional poster for a business shift program"></div>
    </div>
  </aside>
</section>

<section class="book">
  <div class="book-cover img" role="img" aria-label="Book cover mockup"></div>
  <div class="book-copy">
    <h2>Making Womens Power</h2>
    <h3>Book Now on store</h3>
    <p>Nulla sed congue orci. Lorem ipsum dolor sit amet, consectetur adipiscing elit. In sed ornare, tincidunt nibh vitae rhoncus ex, maximus condimentum lorem. Integer vel amet aliquet nulla, ut fermentum libero. Interdum et malesuada fames ac ante ipsum primis in faucibus. Morbi vulputate ipsum lacus, vitae tincidunt diam. Ut sit amet ultrices felis, vulputate faucibus erat.</p>
  </div>
  <div class="store-badge" role="img" aria-label="Online store badge"></div>
</section>

<section class="stream">
  <h2>Elle Marwood on Snapwall</h2>
  <div class="stream-row">
    <div class="img" role="img" aria-label="Gallery photo of the coach at an event" style="background:#6a5448"></div>
    <div class="img" role="img" aria-label="Gallery photo of a workshop" style="background:#c9b8a8"></div>
    <div class="img" role="img" aria-label="Gallery photo of a speaker on stage" style="background:#8a9aa8"></div>
    <div class="img" role="img" aria-label="Gallery photo of a group session" style="background:#d9c7b6"></div>
    <div class="img" role="img" aria-label="Gallery photo of a client meeting" style="background:#4e4a52"></div>
    <div class="img" role="img" aria-label="Gallery photo of a book signing" style="background:#b79a84"></div>
    <div class="img" role="img" aria-label="Gallery photo of a networking evening" style="background:#7c8c96"></div>
    <div class="img" role="img" aria-label="Gallery portrait of the coach" style="background:#3f3a3a"></div>
  </div>
</section>

<section class="partners">
  <span>Norvex</span><span>Ashcombe</span><span>YOURLOGO</span><span>Halden</span>
</section>

<footer class="site-footer">© 2023 Elle Marwood Coaching. All rights reserved.</footer>

</body>
</html>
```